Brand new website for global research and investment startup

We need a simple website, maybe 3 pages: landing page with business description, investment philosophy, team and contact info.
We have a logo already that can be incorporated. Please use the logo only, not the text
We like the color green, something along the lines of #3D6C32 as the main color.
We'd like to design the website with geometric shapes in gradations of the base color. The shapes should suggest "work in progress", "built to last (a long time)", "solidity" and "indestructibility". One idea floating in my head sees smaller features with icosahedron and dodecahedron shapes, and maybe larger structures like crystal lattices; but please feel free to be creative and imagine your own.

```html
<!DOCTYPE html>
<html lang="en">
<head>
<meta charset="utf-8">
<title>Team — Halden</title>
<link rel="stylesheet" href="https://fonts.googleapis.com/css2?family=Manrope:wght@600;700;800&family=Inter:wght@400;500;600&display=swap">
<style>
:root{
  --green:#3D6C32;
  --green-dark:#2a5a2c;
  --ink-green:#284634;
  --ink:#0d0d0d;
  --text:#3b3f45;
  --muted:#8a9096;
  --line:#dfe3df;
  --tint:#f5f8f3;
  --white:#ffffff;
}
*{box-sizing:border-box;margin:0;padding:0}
html,body{width:1042px;height:1200px;overflow:hidden;background:var(--white)}
body{font-family:"Inter",sans-serif;color:var(--text);position:relative}
.site-header{position:absolute;top:0;left:72px;right:72px;height:60px}
.brand{position:absolute;left:0;top:22px;font-family:"Manrope",sans-serif;font-weight:800;font-size:17px;color:var(--green-dark);display:flex;align-items:center;gap:7px}
.brand-mark{width:11px;height:11px;background:currentColor}
.main-nav{position:absolute;left:300px;top:28px;display:flex;gap:0}
.main-nav a{font-size:13px;color:var(--muted);text-decoration:none;padding:0 12px 14px;width:82px;text-align:center}
.main-nav a.active{color:var(--green);font-weight:500;border-bottom:2px solid var(--green)}
.cta{position:absolute;right:0;top:22px;width:105px;height:32px;background:var(--green-dark);color:var(--white);font-size:11.5px;display:flex;align-items:center;justify-content:center;text-decoration:none}
.hero{position:absolute;left:72px;top:144px;width:600px}
.eyebrow{font-size:10px;letter-spacing:.08em;color:var(--green);text-transform:uppercase;margin-bottom:12px}
.hero h1{font-family:"Manrope",sans-serif;font-weight:800;font-size:46px;line-height:56px;letter-spacing:-.01em}
.hero h1 .l1,.hero h1 .l3{color:var(--ink-green);display:block}
.hero h1 .l1{font-weight:700}
.hero h1 .l2{color:var(--ink);display:block}
.lead{font-size:17.4px;line-height:26px;margin-top:12px;width:560px;color:#3d434a}
.team-grid{position:absolute;left:72px;top:471px;width:898px;display:grid;grid-template-columns:repeat(3,283px);grid-auto-rows:277px;gap:23px 24px}
.member{position:relative;border:1px solid var(--line);border-radius:6px;padding:23px 23px 0;background:var(--white)}
.member.featured{background:var(--tint);border-color:#eef2ec}
.portrait{width:58px;height:58px;border-radius:50%;border:1px solid var(--green);background:linear-gradient(160deg,#7a6a5c,#b9a897 45%,#3e4f66)}
.shape{position:absolute;right:20px;top:20px;width:24px;height:24px}
.member h2{font-family:"Manrope",sans-serif;font-weight:700;font-size:14.5px;color:var(--ink);margin-top:28px}
.role{font-size:8.3px;letter-spacing:.1em;color:var(--green);text-transform:uppercase;margin-top:6px;font-weight:500}
.bio{font-size:10.2px;line-height:14.5px;color:#4a5057;margin-top:11px}
.meta{position:absolute;left:23px;right:23px;top:226px;border-top:1px solid #eceeec;display:flex;justify-content:space-between;align-items:center;height:30px;padding-top:2px}
.location{font-size:8.3px;letter-spacing:.1em;color:var(--muted)}
.bio-link{font-size:10px;font-weight:600;color:var(--ink-green);display:flex;align-items:center;gap:6px;text-decoration:none}
.site-footer{position:absolute;left:0;right:0;top:1118px;height:82px;background:var(--green)}
.site-footer .brand{left:70px;top:30px;color:var(--white)}
.footer-nav{position:absolute;left:365px;top:33px;display:flex;gap:17px}
.footer-nav a{color:var(--white);font-size:11px;letter-spacing:.06em;text-decoration:none}
.copyright{position:absolute;right:70px;top:34px;font-size:10px;color:#a9c0a3}
</style>
</head>
<body>
<header class="site-header">
  <div class="brand"><span class="brand-mark"></span>Halden</div>
  <nav class="main-nav">
    <a href="#">Home</a><a href="#" class="active">Team</a><a href="#">Contact</a>
  </nav>
  <a class="cta" href="#">Get in Touch</a>
</header>

<section class="hero">
  <p class="eyebrow">Leadership &amp; Council</p>
  <h1><span class="l1">Guided by empirical</span><span class="l2">minds and institutional</span><span class="l3">stewards.</span></h1>
  <p class="lead">Our leadership team combines deep mathematical research, engineering domain expertise, and decades of global investment execution.</p>
</section>

<main class="team-grid">
  <article class="member featured">
    <div class="portrait" role="img" aria-label="Portrait of Dr. Alaric Venn"></div>
    <svg class="shape" viewBox="0 0 24 24"><path d="M12 2 22 12 12 22 2 12Z" fill="none" stroke="#dde3dd"/></svg>
    <h2>Dr. Alaric Venn</h2>
    <p class="role">Chief Managing Partner</p>
    <p class="bio">Former Head of Quantitative Strategy at Fenbridge Applied Research. Over 22 years experience in macro system dynamics and global equity underwriting.</p>
    <div class="meta"><span class="location">LOCATION: ZURICH</span><a class="bio-link" href="#">Bio <svg width="6" height="9" viewBox="0 0 6 9"><path d="M1 1l3.5 3.5L1 8" fill="none" stroke="currentColor" stroke-width="1.2"/></svg></a></div>
  </article>
  <article class="member">
    <div class="portrait" role="img" aria-label="Portrait of Irena Kostova" style="background:linear-gradient(160deg,#e7ddd2,#a7805e 50%,#d8d2cb)"></div>
    <svg class="shape" viewBox="0 0 24 24"><path d="M12 2 22 22H2Z" fill="none" stroke="#dde3dd"/></svg>
    <h2>Irena Kostova</h2>
    <p class="role">Head of Global Research</p>
    <p class="bio">Directed interdisciplinary supply chain research at Straits Tech Institute. Expert in energy transition infrastructure and materials science investments.</p>
    <div class="meta"><span class="location">LOCATION: SINGAPORE</span><a class="bio-link" href="#">Bio <svg width="6" height="9" viewBox="0 0 6 9"><path d="M1 1l3.5 3.5L1 8" fill="none" stroke="currentColor" stroke-width="1.2"/></svg></a></div>
  </article>
  <article class="member">
    <div class="portrait" role="img" aria-label="Portrait of Martin Thrale" style="background:linear-gradient(160deg,#9fb0a8,#6f7479 50%,#3a3d42)"></div>
    <svg class="shape" viewBox="0 0 24 24"><circle cx="12" cy="12" r="10.5" fill="none" stroke="#dde3dd"/></svg>
    <h2>Martin Thrale</h2>
    <p class="role">Chief Investment Officer</p>
    <p class="bio">20+ years managing private asset allocations across North America and Europe. Focuses on structural risk underwriting and enduring portfolio architecture.</p>
    <div class="meta"><span class="location">LOCATION: NEW YORK</span><a class="bio-link" href="#">Bio <svg width="6" height="9" viewBox="0 0 6 9"><path d="M1 1l3.5 3.5L1 8" fill="none" stroke="currentColor" stroke-width="1.2"/></svg></a></div>
  </article>
  <article class="member">
    <div class="portrait" role="img" aria-label="Portrait of Dr. Kenji Tamura" style="background:linear-gradient(160deg,#b56a58,#8a5a4c 50%,#2f3440)"></div>
    <svg class="shape" viewBox="0 0 24 24"><path d="M12 2 21 7v10l-9 5-9-5V7Z" fill="none" stroke="#dde3dd"/></svg>
    <h2>Dr. Kenji Tamura</h2>
    <p class="role">Director, Deep Technology</p>
    <p class="bio">Quantum computing researcher and semiconductor architect. Leads empirical evaluation of deep hardware breakthroughs and semiconductor supply chains.</p>
    <div class="meta"><span class="location">LOCATION: TOKYO</span><a class="bio-link" href="#">Bio <svg width="6" height="9" viewBox="0 0 6 9"><path d="M1 1l3.5 3.5L1 8" fill="none" stroke="currentColor" stroke-width="1.2"/></svg></a></div>
  </article>
  <article class="member">
    <div class="portrait" role="img" aria-label="Portrait of Camille de Saint-Aubin" style="background:linear-gradient(160deg,#c9d3da,#8a9aa8 50%,#4a6a8e)"></div>
    <svg class="shape" viewBox="0 0 24 24"><circle cx="12" cy="12" r="10.5" fill="none" stroke="#dde3dd"/><path d="M12 1.5v21M1.5 12h21" stroke="#dde3dd"/></svg>
    <h2>Camille de Saint-Aubin</h2>
    <p class="role">Partner, Sustainable Infrastructure</p>
    <p class="bio">Specialized in cross-border grid modernization and municipal infrastructure resilience. Former advisor to the Continental Development Bank.</p>
    <div class="meta"><span class="location">LOCATION: LONDON</span><a class="bio-link" href="#">Bio <svg width="6" height="9" viewBox="0 0 6 9"><path d="M1 1l3.5 3.5L1 8" fill="none" stroke="currentColor" stroke-width="1.2"/></svg></a></div>
  </article>
  <article class="member">
    <div class="portrait" role="img" aria-label="Portrait of Rohan Menon" style="background:linear-gradient(160deg,#2a2d33,#6d6e72 50%,#1b2a44)"></div>
    <svg class="shape" viewBox="0 0 24 24"><path d="M12 2 22 12 12 22 2 12Z" fill="none" stroke="#dde3dd"/><circle cx="12" cy="12" r="3.5" fill="#e6ebe6"/></svg>
    <h2>Rohan Menon</h2>
    <p class="role">Director, Quantitative Systems</p>
    <p class="bio">Lead architect of Halden's proprietary macro simulation engine. Oversees mathematical risk modeling and portfolio equilibrium frameworks.</p>
    <div class="meta"><span class="location">LOCATION: LONDON</span><a class="bio-link" href="#">Bio <svg width="6" height="9" viewBox="0 0 6 9"><path d="M1 1l3.5 3.5L1 8" fill="none" stroke="currentColor" stroke-width="1.2"/></svg></a></div>
  </article>
</main>

<footer class="site-footer">
  <div class="brand"><span class="brand-mark"></span>Halden</div>
  <nav class="footer-nav"><a href="#">Team</a><a href="#">Contact</a><a href="#">Privacy Policy</a><a href="#">Terms &amp; Conditions</a></nav>
  <p class="copyright">© 2026 . All rights reserved.</p>
</footer>
</body>
</html>
```